Redesign wellness clinic website

The project is redesign a wellness clinic http://www.thornleighvitality.example. The new website is to be responsive,clean,bright and a strong call to action which is to book an appointment. The logo will remain the same but the colour scheme on the website should be reflect purple white and green. I want it to be bright and cheerful and the feeling of clarity. The website shouldn't be overloaded with content but more visuals.

Target Market(s)

Anyone that has corporate wellness benefits within the downtown Toronto core. Majority of audience are professional working in Media, Telecommunications and Investments.

Industry/Entity Type

Health And Wellness

Number of Pages Required

5+ page

Font styles to use
Sans Serif

Colors
ffffff
886aae
acd036

Requirements
Must have
• -Strong call to action which is book an appointment like this page https://www.kestrelmotion.example/
• -Services provided icons on the page like https://www.brightpathvitalityhouse.example/
• - Pictures of a good visualizing a fit and healthy life
• - Strong ratings from Quorva, Zintrel, PostMaz, similar to this website http://www.summitbalancehealth.example/our-team-professionals/
• - Bright and clear
Should not have
• -No black and white images (redo our pictures)
• -Dark themes

```html
<!DOCTYPE html>
<html lang="en">
<head>
<meta charset="utf-8">
<title>Thornleigh Vitality Centre</title>
<link href="https://fonts.googleapis.com/css2?family=Poppins:wght@400;500;600;700&display=swap" rel="stylesheet">
<style>
:root{
  --purple:#886aae;
  --purple-dark:#6f5394;
  --purple-soft:#a58bc6;
  --green:#acd036;
  --green-dark:#8fb222;
  --white:#ffffff;
  --ink:#3a3a3a;
  --muted:#7a7a7a;
  --light:#f4f4f4;
  --footer:#2a2a2a;
}
*{box-sizing:border-box;margin:0;padding:0}
html,body{width:1200px;height:3260px;overflow:hidden}
body{font-family:"Poppins",sans-serif;color:var(--ink);background:var(--white);font-size:13px;line-height:1.6}
a{color:inherit;text-decoration:none}
.btn{display:inline-block;background:var(--green);color:var(--white);font-weight:600;font-size:12px;padding:9px 22px;border-radius:22px;letter-spacing:.5px}

/* header */
.site-header{height:64px;display:flex;align-items:center;justify-content:space-between;padding:0 120px}
.brand{display:flex;align-items:center;gap:10px;font-weight:700;color:var(--purple);font-size:17px;letter-spacing:.5px}
.brand-mark{width:34px;height:34px;background:var(--green);border-radius:50%}
.header-actions{display:flex;align-items:center;gap:26px}
.phone{display:flex;align-items:center;gap:8px;color:var(--purple);font-weight:600;font-size:16px}
.main-nav{height:40px;background:var(--purple);display:flex;justify-content:center;gap:54px;align-items:center;color:var(--white);font-size:13px;font-weight:500}

/* hero */
.hero{position:relative;height:576px}
.hero-photo{position:absolute;inset:0;background:linear-gradient(110deg,#d9dde0 0%,#eceef0 35%,#b8c7cf 60%,#7fa6b3 100%)}
.hero-card{position:absolute;right:150px;top:150px;width:420px;background:rgba(255,255,255,.82);padding:30px 34px}
.hero-card h1{font-size:40px;color:var(--purple);font-weight:600;letter-spacing:1px;line-height:1.1;margin-bottom:12px}
.hero-card p{font-size:12px;color:var(--muted);margin-bottom:12px}
.ticks{list-style:none;margin-bottom:18px}
.ticks li{display:flex;align-items:center;gap:8px;font-size:13px;margin-bottom:4px}
.slide-arrow{position:absolute;top:270px;width:34px;height:34px;display:flex;align-items:center;justify-content:center}
.slide-arrow.left{left:20px}.slide-arrow.right{right:20px}

/* welcome */
.welcome{height:280px;display:flex;gap:40px;padding:40px 120px 0}
.welcome-text{flex:1}
.section-title{font-size:24px;font-weight:700;color:var(--ink);text-transform:uppercase;display:flex;align-items:center;gap:10px}
.section-title .accent{color:var(--purple)}
.title-bar{width:4px;height:28px;background:var(--green)}
.welcome-text p{color:var(--muted);font-size:12px;margin:14px 0 18px}
.hours{width:320px;height:180px;background:var(--purple);color:var(--white);padding:22px 26px}
.hours h3{font-size:18px;font-weight:600;margin-bottom:14px}
.hours table{width:100%;font-size:12px;border-collapse:collapse}
.hours td{padding:4px 0}
.hours td:last-child{text-align:right}

/* services */
.services{height:360px;background:var(--light);text-align:center;padding-top:46px}
.center-title{font-size:26px;font-weight:700;text-transform:uppercase}
.underline{width:60px;height:3px;background:var(--green);margin:8px auto 14px}
.services .intro{font-size:11px;color:var(--muted);width:760px;margin:0 auto 30px}
.service-row{display:flex;justify-content:center;gap:60px;align-items:flex-start;position:relative}
.service{width:130px}
.service-icon{width:100px;height:100px;border-radius:50%;border:3px solid var(--green);background:var(--white);margin:0 auto 12px;display:flex;align-items:center;justify-content:center}
.service-icon span{width:50px;height:50px;border-radius:50%;background:var(--purple-soft)}
.service h4{font-size:13px;font-weight:600;text-transform:uppercase}
.svc-arrow{position:absolute;top:38px}
.svc-arrow.left{left:150px}.svc-arrow.right{right:150px}

/* band */
.cta-band{height:260px;background:linear-gradient(90deg,var(--purple-dark),var(--purple),var(--purple-dark));color:var(--white);text-align:center;padding-top:72px}
.cta-band p{width:720px;margin:0 auto 16px;font-size:13px}
.cta-band h3{font-size:15px;font-weight:600;letter-spacing:.5px}
.cta-band .email{font-size:16px;font-weight:500}

/* blog */
.blog{height:600px;padding-top:60px;text-align:center}
.posts{display:flex;gap:40px;padding:10px 120px 0;text-align:left}
.post{flex:1}
.post-head{display:flex;gap:12px;margin-bottom:14px}
.date{width:50px;height:50px;background:var(--green);color:var(--white);text-align:center;font-weight:700;line-height:1.1;padding-top:8px;flex-shrink:0}
.date small{display:block;font-size:10px;font-weight:500}
.post h4{font-size:14px;font-weight:600;line-height:1.35}
.post p{font-size:11.5px;color:var(--muted);margin-bottom:12px}
.read{color:var(--purple);font-weight:600;font-size:12px}

/* reviews */
.reviews{height:560px;background:#eeeeee;display:flex;justify-content:center;gap:60px;padding-top:80px}
.review-card{width:280px;height:400px;background:var(--white);box-shadow:0 4px 14px rgba(0,0,0,.08);display:flex;flex-direction:column;align-items:center;text-align:center;overflow:hidden}
.stars{color:#f5b50a;font-size:22px;letter-spacing:3px;margin:46px 0 18px}
.platform{font-size:40px;font-weight:700;color:var(--purple);height:150px;display:flex;align-items:center}
.review-cta{margin-top:auto;width:100%;height:140px;background:var(--green);color:var(--white);font-weight:600;font-size:14px;display:flex;align-items:center;justify-content:center;padding:0 40px}

/* footer */
.site-footer{height:480px;background:var(--footer);color:#d8d8d8;display:flex;gap:60px;padding:90px 120px 0}
.foot-col{flex:1;font-size:12px}
.map{height:130px;background:linear-gradient(135deg,#e2e6d8,#c9d4b8);margin-bottom:18px}
.contact-line{display:flex;align-items:center;gap:10px;margin-bottom:8px}
.foot-col h3{font-size:18px;color:var(--white);font-weight:600;margin-bottom:18px;display:flex;align-items:center;gap:10px}
.tweet{display:flex;gap:12px;margin-bottom:18px}
.avatar{width:38px;height:38px;border-radius:50%;background:var(--purple);flex-shrink:0}
.tweet strong{color:var(--white);font-weight:500}
.badge{width:120px;height:150px;background:#e08a2a;margin:0 auto 16px;border-radius:4px}
.foot-col.right{text-align:center}
.bottom-bar{height:40px;background:var(--purple);color:var(--white);font-size:11px;text-align:center;line-height:40px}
</style>
</head>
<body>

<header class="site-header">
  <div class="brand"><span class="brand-mark"></span>THORNLEIGH VITALITY CENTRE</div>
  <div class="header-actions">
    <a class="btn" href="#">BOOK AN APPOINTMENT</a>
    <div class="phone">
      <svg width="18" height="18" viewBox="0 0 24 24"><path fill="#886aae" d="M6.6 10.8a15 15 0 0 0 6.6 6.6l2.2-2.2a1 1 0 0 1 1-.25 11.4 11.4 0 0 0 3.6.6 1 1 0 0 1 1 1V20a1 1 0 0 1-1 1A17 17 0 0 1 3 4a1 1 0 0 1 1-1h3.5a1 1 0 0 1 1 1c0 1.25.2 2.45.6 3.6a1 1 0 0 1-.25 1z"/></svg>
      416-555-0142
    </div>
  </div>
</header>
<nav class="main-nav">
  <a href="#">Home</a><a href="#">Fees and Services</a><a href="#">Our Staff</a><a href="#">News and Updates</a><a href="#">Corporate Wellness</a><a href="#">Forms</a><a href="#">Contact</a>
</nav>

<section class="hero">
  <div class="hero-photo" role="img" aria-label="Photo of a chiropractor adjusting a patient's shoulder in a bright clinic"></div>
  <div class="slide-arrow left"><svg width="20" height="30"><path d="M15 3 4 15l11 12" stroke="#fff" stroke-width="3" fill="none"/></svg></div>
  <div class="slide-arrow right"><svg width="20" height="30"><path d="M5 3l11 12L5 27" stroke="#fff" stroke-width="3" fill="none"/></svg></div>
  <div class="hero-card">
    <h1>CHIROPRACTIC</h1>
    <p>Established in 1995 the Thornleigh Vitality Centre has become one of Toronto's leaders in providing quality care.</p>
    <ul class="ticks">
      <li><svg width="14" height="14"><circle cx="7" cy="7" r="7" fill="#acd036"/><path d="M3.5 7l2.3 2.3L10.5 4.7" stroke="#fff" stroke-width="1.8" fill="none"/></svg>Adjustment</li>
      <li><svg width="14" height="14"><circle cx="7" cy="7" r="7" fill="#acd036"/><path d="M3.5 7l2.3 2.3L10.5 4.7" stroke="#fff" stroke-width="1.8" fill="none"/></svg>Functional Adjustment</li>
      <li><svg width="14" height="14"><circle cx="7" cy="7" r="7" fill="#acd036"/><path d="M3.5 7l2.3 2.3L10.5 4.7" stroke="#fff" stroke-width="1.8" fill="none"/></svg>Custom Orthotics and Bracing</li>
    </ul>
    <a class="btn" href="#">BOOK AN APPOINTMENT</a>
  </div>
</section>

<section class="welcome">
  <div class="welcome-text">
    <h2 class="section-title"><span class="title-bar"></span>Welcome to <span class="accent">Thornleigh Vitality Centre</span></h2>
    <p>Established in 1995 the Thornleigh Vitality Centre has become one of Toronto's leaders in providing quality, holistic wellness programs for the community. Our founders were driven to create a team where clients come to be well cared for, and all practitioners work together under one roof. Some of the services include chiropractic, physiotherapy, active rehabilitation, massage therapy, osteopathy and personal training so every client can reach their goals with ease.</p>
    <a class="btn" href="#" style="background:var(--purple)">READ MORE</a>
  </div>
  <aside class="hours">
    <h3>OPENING HOURS</h3>
    <table>
      <tr><td>Monday - Friday</td><td>7:00am - 9pm</td></tr>
      <tr><td>Saturday</td><td>9:00am - 3pm</td></tr>
      <tr><td>Sunday</td><td>10am - 3pm</td></tr>
    </table>
  </aside>
</section>

<section class="services">
  <h2 class="center-title">Our Services</h2>
  <div class="underline"></div>
  <p class="intro">Simple care plans built around you, with friendly practitioners who work together to help you feel strong, move freely and stay well.</p>
  <div class="service-row">
    <svg class="svc-arrow left" width="16" height="26"><path d="M13 2 3 13l10 11" stroke="#886aae" stroke-width="3" fill="none"/></svg>
    <div class="service"><div class="service-icon" role="img" aria-label="Chiropractic icon"><span></span></div><h4>Chiropractic</h4></div>
    <div class="service"><div class="service-icon" role="img" aria-label="Physiotherapy icon"><span></span></div><h4>Physiotherapy</h4></div>
    <div class="service"><div class="service-icon" role="img" aria-label="Active rehabilitation icon"><span></span></div><h4>Active Rehabilitation</h4></div>
    <div class="service"><div class="service-icon" role="img" aria-label="Massage therapy icon"><span></span></div><h4>Massage Therapy</h4></div>
    <div class="service"><div class="service-icon" role="img" aria-label="Osteopathy icon"><span></span></div><h4>Osteopathy</h4></div>
    <svg class="svc-arrow right" width="16" height="26"><path d="M3 2l10 11L3 24" stroke="#886aae" stroke-width="3" fill="none"/></svg>
  </div>
</section>

<section class="cta-band">
  <p>Our Centre is committed to helping improve and extend the lives of as many people as possible in our community. Come and join our family and start managing your life today.</p>
  <h3>PLANNING A WELLNESS TRIP? WE CAN HELP!</h3>
  <div class="email">info@thornleighvitality.example</div>
</section>

<section class="blog">
  <h2 class="center-title">From the Blog</h2>
  <div class="underline"></div>
  <div class="posts">
    <article class="post">
      <div class="post-head"><div class="date">05<small>JUN</small></div><h4>DOLOR SIT AMET, CONSECTETUR ELIT, SED DIAM NONUMMY</h4></div>
      <p>Small daily habits add up. Learn how short stretching breaks at your desk can ease tension in your neck, back and shoulders during long working days.</p>
      <p>Our team shares simple moves you can do in minutes, plus tips on posture and screen height that help keep you feeling fresh and focused.</p>
      <a class="read" href="#">Read More</a>
    </article>
    <article class="post">
      <div class="post-head"><div class="date">12<small>JUN</small></div><h4>DOLOR SIT AMET, CONSECTETUR ELIT, SED DIAM NONUMMY</h4></div>
      <p>Massage therapy is more than a treat. Regular sessions support recovery, lower stress and help muscles stay supple between workouts and busy weeks.</p>
      <p>Find out what to expect at your first visit, how often to book, and how your corporate benefits can cover the cost of ongoing care.</p>
      <a class="read" href="#">Read More</a>
    </article>
    <article class="post">
      <div class="post-head"><div class="date">19<small>JUN</small></div><h4>DOLOR SIT AMET, CONSECTETUR ELIT, SED DIAM NONUMMY</h4></div>
      <p>Getting back to running after an injury takes patience. Our physiotherapists explain how a guided plan rebuilds strength safely and step by step.</p>
      <p>We cover warm ups, pacing and the warning signs to watch for, so you can return to the activities you love with real confidence.</p>
      <a class="read" href="#">Read More</a>
    </article>
  </div>
</section>

<section class="reviews">
  <div class="review-card">
    <div class="stars">★★★★★</div>
    <div class="platform">Quorva</div>
    <a class="review-cta" href="#">Click To See Our Reviews On Quorva</a>
  </div>
  <div class="review-card">
    <div class="stars">★★★★★</div>
    <div class="platform">Zintrel</div>
    <a class="review-cta" href="#">Click To See Our Reviews On Zintrel</a>
  </div>
  <div class="review-card">
    <div class="stars">★★★★★</div>
    <div class="platform">PostMaz</div>
    <a class="review-cta" href="#">Click To See Our Reviews On PostMaz</a>
  </div>
</section>

<footer class="site-footer">
  <div class="foot-col">
    <div class="map" role="img" aria-label="Street map showing the clinic location"></div>
    <div class="contact-line"><svg width="14" height="16"><path d="M7 0a5.5 5.5 0 0 0-5.5 5.5C1.5 10 7 16 7 16s5.5-6 5.5-10.5A5.5 5.5 0 0 0 7 0zm0 7.5a2 2 0 1 1 0-4 2 2 0 0 1 0 4z" fill="#acd036"/></svg>Thornleigh Vitality Centre, 12 Harrow Lane, Suite 200, Toronto, Ontario</div>
    <div class="contact-line"><svg width="14" height="12"><rect width="14" height="12" rx="1" fill="#acd036"/><path d="M0 1l7 5 7-5" stroke="#2a2a2a" fill="none"/></svg>info@thornleighvitality.example</div>
    <div class="contact-line"><svg width="14" height="14" viewBox="0 0 24 24"><path fill="#acd036" d="M6.6 10.8a15 15 0 0 0 6.6 6.6l2.2-2.2a1 1 0 0 1 1-.25 11.4 11.4 0 0 0 3.6.6 1 1 0 0 1 1 1V20a1 1 0 0 1-1 1A17 17 0 0 1 3 4a1 1 0 0 1 1-1h3.5a1 1 0 0 1 1 1c0 1.25.2 2.45.6 3.6a1 1 0 0 1-.25 1z"/></svg>416-555-0142</div>
    <div class="contact-line"><svg width="14" height="14" viewBox="0 0 24 24"><path fill="#acd036" d="M6.6 10.8a15 15 0 0 0 6.6 6.6l2.2-2.2a1 1 0 0 1 1-.25 11.4 11.4 0 0 0 3.6.6 1 1 0 0 1 1 1V20a1 1 0 0 1-1 1A17 17 0 0 1 3 4a1 1 0 0 1 1-1h3.5a1 1 0 0 1 1 1c0 1.25.2 2.45.6 3.6a1 1 0 0 1-.25 1z"/></svg>416-555-0143</div>
  </div>
  <div class="foot-col">
    <h3><svg width="14" height="14"><circle cx="7" cy="7" r="7" fill="#886aae"/></svg>LATEST TWEET</h3>
    <div class="tweet"><span class="avatar"></span><div><strong>Thornleigh Vitality</strong> @ThornleighVital<br>New evening massage slots open this week. Book today!</div></div>
    <div class="tweet"><span class="avatar"></span><div><strong>Thornleigh Vitality</strong> @ThornleighVital<br>Desk stretches to try between meetings on our blog now.</div></div>
    <div class="tweet"><span class="avatar"></span><div><strong>Thornleigh Vitality</strong> @ThornleighVital<br>Welcome our new osteopath to the team this month!</div></div>
  </div>
  <div class="foot-col right">
    <div class="badge" role="img" aria-label="Local listing award badge"></div>
    <p>Thornleigh Vitality Centre is listed as a top Wellness Centre in Toronto, verified by local reviewers.</p>
  </div>
</footer>
<div class="bottom-bar">© Thornleigh Vitality 2017</div>

</body>
</html>
```